PINE HOLLOW BUILDERS leave behind sales FLYER 8.5"x11"

We need a high quality advertising flyer 8.5"x11" for our construction company offering kitchen and bathroom remodels. Can be front and back or just the front of the flyer depending on the design. phone number to come
www.brightmortarworks.example

we are also a home inspection company. We will leave this at the home when we are done with our home inspections for our new home owners

Target Market(s)

Home owners

Industry/Entity Type

Residential Construction

Contact Information for Business Card

We want it to match the flyer please

Requirements
Must have
• My logo, my website , my phone number (to come later),
• FL State Lic. #CRC8047163 & Insured
• We Specialize in Bathroom and Kitchen remodeling ,new Construction & Interior or Exterior home Renovations, garages and more! Serving Central Florida for over 15 years.
• Family owned and operated,
• we perform all levels of building and remodeling.
• i wouldn't mind seeing what you come up with for text on the flyer.
Nice to have
• maybe a nice kitchen and bathroom pictures

```html
<!DOCTYPE html>
<html lang="en">
<head>
<meta charset="utf-8">
<title>Pine Hollow Builders – Flyer</title>
<link href="https://fonts.googleapis.com/css2?family=Titillium+Web:wght@300;400;600;700&display=swap" rel="stylesheet">
<style>
  :root {
    --orange: #f0921e;
    --orange-dark: #e07f12;
    --blue: #0a77b0;
    --ink: #2f2f2f;
    --grey: #555a5e;
    --white: #ffffff;
    --paper: #ffffff;
  }
  * { margin: 0; padding: 0; box-sizing: border-box; }
  html, body { width: 960px; height: 1200px; overflow: hidden; background: var(--paper); }
  body { font-family: 'Titillium Web', Arial, sans-serif; color: var(--ink); }
  .flyer { position: relative; width: 960px; height: 1200px; background: var(--white); overflow: hidden; }

  .hero-photo {
    position: absolute; left: 0; top: 0; width: 960px; height: 420px;
    background:
      radial-gradient(ellipse at 85% 10%, rgba(255,214,200,.85), rgba(255,214,200,0) 55%),
      linear-gradient(180deg, #b9b4ad 0%, #8f8a84 45%, #a79d92 100%);
  }

  .brand-box {
    position: absolute; left: 74px; top: 0; width: 237px; height: 195px;
    background: var(--white); border-radius: 0 0 10px 10px;
    display: flex; flex-direction: column; align-items: center; justify-content: center; gap: 14px;
  }
  .brand-mark { width: 46px; height: 46px; background: var(--orange); }
  .brand-name {
    font-weight: 700; font-size: 21px; line-height: 1.1; letter-spacing: 1px;
    color: var(--grey); text-align: center;
  }

  .headline {
    position: absolute; left: 47px; top: 268px;
    font-weight: 300; font-size: 62px; line-height: 58px; color: var(--white);
    text-transform: uppercase;
  }

  .specialty-band {
    position: absolute; left: 0; top: 419px; width: 885px; height: 115px;
    background: var(--orange); padding: 22px 0 0 49px; color: var(--white);
  }
  .specialty-band h2 { font-weight: 700; font-size: 34px; line-height: 40px; }
  .specialty-band p { font-weight: 400; font-size: 21px; line-height: 26px; }
  .band-fold { position: absolute; left: 0; top: 0; }

  .service-area {
    position: absolute; left: 0; top: 536px; width: 615px; height: 53px;
    background: var(--blue); clip-path: polygon(0 0, 100% 0, 97% 100%, 0 100%);
    color: var(--white); font-weight: 700; font-size: 23px; line-height: 53px;
    padding-left: 50px; text-transform: uppercase; letter-spacing: .2px;
  }

  .services-title {
    position: absolute; left: 50px; top: 608px;
    color: var(--orange); font-weight: 700; font-size: 29px; line-height: 36px;
    text-transform: uppercase;
  }
  .services-copy {
    position: absolute; left: 50px; top: 648px; width: 480px;
    font-size: 17.5px; line-height: 25.3px; color: var(--ink);
  }
  .services-copy p + p { margin-top: 25px; }

  .service-list {
    position: absolute; top: 648px; list-style: none;
    font-size: 17.5px; line-height: 28px; color: var(--ink);
  }
  .service-list li::before {
    content: ""; display: inline-block; width: 4px; height: 4px;
    background: var(--orange); margin-right: 7px; vertical-align: middle;
  }
  .service-list.col-a { left: 574px; }
  .service-list.col-b { left: 765px; }

  .levels-box {
    position: absolute; left: 546px; top: 804px; width: 414px; height: 66px;
    background: var(--blue); clip-path: polygon(4% 0, 100% 0, 100% 100%, 0 100%);
    color: var(--white); font-weight: 700; font-size: 22px; line-height: 24px;
    padding: 9px 0 0 54px; text-transform: uppercase;
  }

  .gallery { position: absolute; left: 0; top: 898px; width: 960px; height: 178px; display: block; }

  .contact-phone {
    position: absolute; left: 47px; top: 1112px;
    display: flex; align-items: center; gap: 14px;
    font-weight: 600; font-size: 34px; color: var(--grey);
  }
  .contact-web {
    position: absolute; right: 45px; top: 1112px; text-align: right;
  }
  .contact-web .url { font-weight: 600; font-size: 21px; line-height: 26px; color: var(--orange); }
  .contact-web .license { font-size: 14px; line-height: 20px; color: var(--ink); }
</style>
</head>
<body>
<main class="flyer">
  <div class="hero-photo" role="img" aria-label="Photo of a builder in a hard hat and overalls leaping in front of a house with a tiled roof"></div>

  <div class="brand-box">
    <span class="brand-mark"></span>
    <span class="brand-name">PINE HOLLOW<br>BUILDERS</span>
  </div>

  <h1 class="headline">Reliable &amp;<br>Reasonable</h1>

  <svg class="band-fold" width="960" height="540" viewBox="0 0 960 540" aria-hidden="true">
    <polygon points="885,419 960,333 960,447 885,534" fill="var(--orange-dark)"/>
  </svg>
  <section class="specialty-band">
    <h2>We Specialize in Bathroom and Kitchen remodeling,</h2>
    <p>New Construction &amp; Interior or Exterior home Renovations, garages and more!</p>
  </section>

  <div class="service-area">Serving Central Florida for over 15 years</div>

  <h3 class="services-title">Our Services</h3>
  <div class="services-copy">
    <p>Family owned and operated, we perform all levels of building and remodeling. We offer start-to-finish solutions for every project. We specialize in interior or exterior home renovations, including bathroom and kitchen remodeling, home additions, garages and more!</p>
    <p>We guarantee high-quality construction for each and every project. Check out samples of our recent work,and you'll agree that we're the best choice for your home renovation project.</p>
  </div>

  <ul class="service-list col-a">
    <li>New Construction</li>
    <li>Barns</li>
    <li>Remodels</li>
    <li>Renovations</li>
  </ul>
  <ul class="service-list col-b">
    <li>Repairs</li>
    <li>Kitchen</li>
    <li>Bathroom</li>
    <li>Bank Remodels</li>
  </ul>

  <div class="levels-box">We perform all levels of<br>building and remodeling</div>

  <svg class="gallery" viewBox="0 0 960 178" aria-hidden="false">
    <defs>
      <linearGradient id="g1" x1="0" y1="0" x2="0" y2="1"><stop offset="0" stop-color="#cfc9c2"/><stop offset="1" stop-color="#9d938a"/></linearGradient>
      <linearGradient id="g2" x1="0" y1="0" x2="0" y2="1"><stop offset="0" stop-color="#d9c6b2"/><stop offset="1" stop-color="#8f7b69"/></linearGradient>
      <linearGradient id="g3" x1="0" y1="0" x2="0" y2="1"><stop offset="0" stop-color="#d6d3cf"/><stop offset="1" stop-color="#a69a8d"/></linearGradient>
      <linearGradient id="g4" x1="0" y1="0" x2="0" y2="1"><stop offset="0" stop-color="#efe3dc"/><stop offset="1" stop-color="#d8ccc6"/></linearGradient>
    </defs>
    <polygon role="img" aria-label="Photo of a modern kitchen counter" points="0,0 245,0 146,178 0,178" fill="url(#g1)"/>
    <polygon role="img" aria-label="Photo of a bathroom with a clawfoot tub" points="256,0 520,0 425,178 157,178" fill="url(#g2)"/>
    <polygon role="img" aria-label="Photo of a remodeled kitchen with wood cabinets" points="531,0 804,0 704,178 436,178" fill="url(#g3)"/>
    <polygon role="img" aria-label="Photo of a bright modern bathroom" points="815,0 960,0 960,178 715,178" fill="url(#g4)"/>
  </svg>

  <div class="contact-phone">
    <svg width="36" height="36" viewBox="0 0 24 24" fill="none" stroke="var(--orange)" stroke-width="1.5" stroke-linecap="round" stroke-linejoin="round" aria-hidden="true">
      <path d="M22 16.9v3a2 2 0 0 1-2.2 2 19.8 19.8 0 0 1-8.6-3.1 19.5 19.5 0 0 1-6-6A19.8 19.8 0 0 1 2.1 4.2 2 2 0 0 1 4.1 2h3a2 2 0 0 1 2 1.7c.1.9.4 1.8.7 2.7a2 2 0 0 1-.5 2.1L8 9.8a16 16 0 0 0 6 6l1.3-1.3a2 2 0 0 1 2.1-.4c.9.3 1.8.6 2.7.7a2 2 0 0 1 1.7 2z"/>
      <path d="M15 2a7 7 0 0 1 7 7"/>
      <path d="M15 6a3 3 0 0 1 3 3"/>
    </svg>
    <span>123 4567 890</span>
  </div>

  <div class="contact-web">
    <div class="url">www.brightmortarworks.example</div>
    <div class="license">FL State Lic. #CRC8047163 &amp; Insured</div>
  </div>
</main>
</body>
</html>
```